Proposal Template Design

We are looking to have our proposal templates redesigned. attached are examples of what we have been using. as well as our current logo

```html
<!DOCTYPE html>
<html lang="en">
<head>
<meta charset="utf-8">
<title>Ridgeline Foam Co. – Letterhead</title>
<link rel="stylesheet" href="https://fonts.googleapis.com/css2?family=Oswald:wght@300;500&family=Roboto+Condensed:wght@700&family=Montserrat:wght@600&display=swap">
<style>
  :root {
    --backdrop: #ececec;
    --paper: #ffffff;
    --ink: #060708;
    --blue-deep: #1257a8;
    --blue-bright: #18a2dc;
    --separator: #e6e7e8;
    --fade: #efefef;
  }
  * { margin: 0; padding: 0; box-sizing: border-box; }
  html, body { width: 1200px; height: 824px; overflow: hidden; background: var(--backdrop); }
  .canvas { position: relative; width: 1200px; height: 824px; }
  .sheet { position: absolute; top: 81px; width: 461px; height: 653px; background: var(--paper); }
  .sheet--dark-header { left: 86px; }
  .sheet--blue-header { left: 638px; }
  .sheet svg { display: block; width: 100%; height: 100%; }

  .brand-name { font-family: "Roboto Condensed", sans-serif; font-weight: 700; font-size: 34px; fill: var(--paper); }
  .contact-line { font-family: "Oswald", sans-serif; font-weight: 300; font-size: 16px; fill: var(--paper); }
  .phone-number { font-family: "Montserrat", sans-serif; font-weight: 600; font-size: 21px; letter-spacing: 1px; fill: var(--ink); }
  .service-list { font-family: "Oswald", sans-serif; font-weight: 500; font-size: 21px; fill: var(--paper); letter-spacing: 0.3px; }
  .icon-disc { fill: var(--paper); }
  .icon-mark { fill: var(--ink); }
  .phone-disc { fill: var(--ink); }
  .separator { fill: var(--separator); }
  .footer-fade { fill: url(#fadeGrad); }

  .sheet--dark-header .header-outer, .sheet--dark-header .footer-right { fill: url(#blueGrad); }
  .sheet--dark-header .header-block, .sheet--dark-header .contact-bar, .sheet--dark-header .footer-left { fill: var(--ink); }
  .sheet--blue-header .header-outer, .sheet--blue-header .footer-right { fill: var(--ink); }
  .sheet--blue-header .header-block, .sheet--blue-header .contact-bar, .sheet--blue-header .footer-left { fill: url(#blueGrad); }
  .sheet--blue-header .icon-mark { fill: var(--blue-deep); }
</style>
</head>
<body>
<svg width="0" height="0" style="position:absolute" aria-hidden="true">
  <defs>
    <linearGradient id="blueGrad" x1="0" y1="0" x2="1" y2="0">
      <stop offset="0" stop-color="#1257a8"/>
      <stop offset="1" stop-color="#18a2dc"/>
    </linearGradient>
    <linearGradient id="fadeGrad" x1="0" y1="0" x2="0" y2="1">
      <stop offset="0" stop-color="#ffffff"/>
      <stop offset="1" stop-color="#efefef"/>
    </linearGradient>
    <symbol id="pin" viewBox="0 0 24 24">
      <circle class="icon-disc" cx="12" cy="12" r="12"/>
      <path class="icon-mark" d="M12 5a5 5 0 0 0-5 5c0 3.6 5 9 5 9s5-5.4 5-9a5 5 0 0 0-5-5zm0 7a2 2 0 1 1 0-4 2 2 0 0 1 0 4z"/>
    </symbol>
    <symbol id="mail" viewBox="0 0 24 24">
      <circle class="icon-disc" cx="12" cy="12" r="12"/>
      <path class="icon-mark" d="M5.5 8h13v8.5h-13zm1.6 1.2 4.9 3.6 4.9-3.6zm-.4 1v5.1h10.6v-5.1l-5.3 3.9z"/>
    </symbol>
    <symbol id="phone" viewBox="0 0 24 24">
      <circle class="phone-disc" cx="12" cy="12" r="12"/>
      <path fill="#fff" d="M8.6 5.8c.5-.3 1 0 1.2.4l1.1 2.3c.2.4.1.9-.3 1.2l-.9.7c.6 1.4 1.6 2.5 3 3.1l.7-.9c.3-.4.8-.5 1.2-.3l2.3 1.1c.5.2.7.7.4 1.2l-.8 1.4c-.3.5-.9.8-1.5.7-4-.8-7.1-3.9-7.9-7.9-.1-.6.2-1.2.7-1.5z"/>
    </symbol>
  </defs>
</svg>

<main class="canvas">
  <section class="sheet sheet--dark-header" aria-label="Letterhead, dark header version">
    <svg viewBox="0 0 893 1263" preserveAspectRatio="none">
      <rect class="footer-fade" x="0" y="960" width="893" height="271"/>
      <path class="header-outer" d="M0 0H893V34H470C430 34 405 62 400 105C394 160 352 199 292 199H0Z"/>
      <path class="separator" d="M0 0H320C372 0 400 42 400 92C400 146 362 180 308 180H0Z"/>
      <path class="header-block" d="M0 0H308C352 0 372 40 372 88C372 138 346 176 300 176H0Z"/>
      <text class="brand-name" x="162" y="100" text-anchor="middle">Ridgeline</text>
      <text class="brand-name" x="162" y="140" text-anchor="middle">Foam Co.</text>
      <path class="contact-bar" d="M424 100V72C424 50 440 34 466 34H893V100Z"/>
      <use href="#pin" x="450" y="56" width="22" height="22"/>
      <text class="contact-line" x="483" y="73" textLength="192" lengthAdjust="spacingAndGlyphs">P.O. Box 218, Millbrook Texas 75099</text>
      <use href="#mail" x="690" y="56" width="22" height="22"/>
      <text class="contact-line" x="721" y="73" textLength="148" lengthAdjust="spacingAndGlyphs">office@ridgelinefoam.com</text>
      <use href="#phone" x="450" y="110" width="22" height="22"/>
      <text class="phone-number" x="484" y="129" textLength="150" lengthAdjust="spacingAndGlyphs">555-014-2290</text>
      <rect class="footer-left" x="-3" y="1231" width="393" height="32"/>
      <path class="footer-right" d="M398 1263C404 1226 420 1199 462 1199H893V1263Z"/>
      <text class="service-list" x="661" y="1243" text-anchor="middle" textLength="420" lengthAdjust="spacingAndGlyphs">SPRAYFOAM | FIBERGLASS | INSULATION | ROOFING</text>
    </svg>
  </section>

  <section class="sheet sheet--blue-header" aria-label="Letterhead, blue header version">
    <svg viewBox="0 0 893 1263" preserveAspectRatio="none">
      <rect class="footer-fade" x="0" y="960" width="893" height="271"/>
      <path class="header-outer" d="M0 0H893V34H470C430 34 405 62 400 105C394 160 352 199 292 199H0Z"/>
      <path class="separator" d="M0 0H320C372 0 400 42 400 92C400 146 362 180 308 180H0Z"/>
      <path class="header-block" d="M0 0H308C352 0 372 40 372 88C372 138 346 176 300 176H0Z"/>
      <text class="brand-name" x="168" y="100" text-anchor="middle">Ridgeline</text>
      <text class="brand-name" x="168" y="140" text-anchor="middle">Foam Co.</text>
      <path class="contact-bar" d="M424 100V72C424 50 440 34 466 34H893V100Z"/>
      <use href="#pin" x="452" y="56" width="22" height="22"/>
      <text class="contact-line" x="485" y="73" textLength="192" lengthAdjust="spacingAndGlyphs">P.O. Box 218, Millbrook Texas 75099</text>
      <use href="#mail" x="692" y="56" width="22" height="22"/>
      <text class="contact-line" x="723" y="73" textLength="148" lengthAdjust="spacingAndGlyphs">office@ridgelinefoam.com</text>
      <use href="#phone" x="452" y="110" width="22" height="22"/>
      <text class="phone-number" x="486" y="129" textLength="150" lengthAdjust="spacingAndGlyphs">555-014-2290</text>
      <rect class="footer-left" x="-3" y="1231" width="383" height="32"/>
      <path class="footer-right" d="M396 1263C404 1226 420 1199 462 1199H893V1263Z"/>
      <text class="service-list" x="645" y="1243" text-anchor="middle" textLength="420" lengthAdjust="spacingAndGlyphs">SPRAYFOAM | FIBERGLASS | INSULATION | ROOFING</text>
    </svg>
  </section>
</main>
</body>
</html>
```